Golf Day Flyer - Harlowe School

Flyer for a golf day.
Parents and friends of a school are invited to play golf on Monday 22nd October.

Flyer from last year (2017) is attached. We would like to make the flyer more fun/humorous this year.

The golf day has two sessions: (1) Round of golf starting at 9AM and (2) Golf Clinic for beginner golfers.

So the flyer could have two sections - one showing experienced golfers, the other showing beginner golfers.

We have not finalised all the content for the flyer yet but need to look at some designs before we give all the content.

Target Market(s)

parents and friends of the school students - professionals (accountants, lawyers, doctors, etc)

Industry/Entity Type

Golf Course

Font styles to use
Serif

Colors

Designer to choose colors to be used in the design.

Requirements
Must have
• Refer to content attached document
Nice to have
• Funny golf pictures
Should not have
• N/A

```html
<!DOCTYPE html>
<html lang="en">
<head>
<meta charset="utf-8">
<title>Harlowe Golf Day 2018</title>
<link rel="stylesheet" href="https://fonts.googleapis.com/css2?family=Audiowide&family=Noto+Serif:ital,wght@1,700&family=Noto+Sans:ital,wght@0,400;0,700;1,400&display=swap">
<style>
  :root {
    --turf-dark: #1f3a1c;
    --turf-mid: #2e4a2a;
    --sky-top: #3fe0d8;
    --sky-low: #bff5f2;
    --banner-green: #4fb81a;
    --banner-light: #7ee022;
    --lime: #a6ff00;
    --lime-text: #e4ff3a;
    --title-text: #f3ff9a;
    --maroon: #8b0a0a;
    --time-green: #4d6f12;
    --deep-green: #1d3f12;
    --panel-black: #0d0d0d;
    --white: #ffffff;
    --ball: #c9ccd2;
  }
  * { box-sizing: border-box; margin: 0; padding: 0; }
  html, body { width: 856px; height: 1200px; overflow: hidden; background: var(--turf-dark); }
  .flyer {
    position: relative; width: 856px; height: 1200px; overflow: hidden;
    background: radial-gradient(ellipse at 50% 62%, #4a5e45 0%, var(--turf-mid) 40%, var(--turf-dark) 75%),
                var(--turf-dark);
    font-family: "Noto Sans", Verdana, sans-serif;
  }
  .turf-photo { position: absolute; inset: 0; }
  .sky-scene { position: absolute; left: 0; top: 0; width: 856px; height: 330px; }
  .title-banner {
    position: absolute; left: 299px; top: 210px; width: 539px; height: 107px;
    border-radius: 20px;
    background: linear-gradient(180deg, var(--banner-light), var(--banner-green));
    display: flex; align-items: center; padding-left: 80px; gap: 6px;
    font-family: "Audiowide", sans-serif; color: var(--title-text);
    overflow: hidden;
  }
  .title-name, .title-year { font-size: 43px; line-height: 1; white-space: nowrap; }
  .title-tag {
    display: flex; flex-direction: column; font-size: 13px; line-height: 14px;
    transform: rotate(-90deg); width: 30px; text-align: center;
  }
  .session-card { position: absolute; top: 470px; width: 264px; height: 342px; }
  .session-card svg { position: absolute; left: 0; top: 0; }
  .session-left { left: 6px; }
  .session-right { left: 576px; }
  .session-time {
    position: absolute; left: 0; right: 0; top: 156px; text-align: center;
    font-family: "Noto Serif", Georgia, serif; font-style: italic; font-weight: 700;
    font-size: 23px; color: var(--time-green); letter-spacing: 0.5px; white-space: nowrap;
  }
  .session-desc {
    position: absolute; left: 50%; transform: translateX(-50%); width: 200px; top: 226px; text-align: center;
    font-size: 17px; line-height: 21px; letter-spacing: 0.6px; color: var(--maroon);
  }
  .date-ball {
    position: absolute; left: 324px; top: 668px; width: 220px; height: 220px; border-radius: 50%;
    background: radial-gradient(circle at 45% 40%, #d8dbe0, var(--ball) 60%, #a8acb3);
    text-align: center; color: var(--deep-green);
  }
  .date-day { font-family: "Audiowide", sans-serif; font-size: 108px; line-height: 110px; margin-top: 42px; letter-spacing: -4px; }
  .date-month { font-weight: 700; font-size: 18px; letter-spacing: 1px; margin-top: 4px; }
  .lunch-panel {
    position: absolute; left: 185px; top: 910px; width: 495px; height: 186px;
    background: var(--panel-black); border-radius: 16px; text-align: center;
    font-size: 17px; letter-spacing: 0.8px; color: var(--white);
  }
  .lunch-title { font-family: "Audiowide", sans-serif; font-weight: 400; font-size: 23px; letter-spacing: 2px; margin-top: 14px; }
  .lunch-info { margin-top: 12px; line-height: 22px; }
  .lunch-pay { margin-top: 24px; line-height: 27px; }
  .label { color: var(--lime-text); }
  .footer-band {
    position: absolute; left: 0; top: 1124px; width: 856px; height: 76px;
    background: var(--deep-green); display: flex; align-items: center; justify-content: center;
    font-style: italic; font-size: 21px; letter-spacing: 1.8px; color: var(--lime-text); white-space: nowrap;
  }
</style>
</head>
<body>
<main class="flyer">
  <div class="turf-photo" role="img" aria-label="Close-up photo of a golf ball beside the hole on the putting green"></div>

  <svg class="sky-scene" viewBox="0 0 856 330" role="img" aria-label="Illustrated sunny sky with clouds over the sea and a silhouetted golfer mid-swing">
    <defs>
      <linearGradient id="skyFill" x1="0" y1="0" x2="0" y2="1">
        <stop offset="0" stop-color="#3fe0d8"/>
        <stop offset="0.6" stop-color="#bff5f2"/>
        <stop offset="1" stop-color="#ffffff"/>
      </linearGradient>
    </defs>
    <path d="M0 0 H856 V190 C700 260 520 320 300 328 C160 332 60 318 0 300 Z" fill="url(#skyFill)"/>
  </svg>

  <header class="title-banner">
    <span class="title-name">HARLOWE</span>
    <span class="title-tag"><span>GOLF</span><span>DAY</span></span>
    <span class="title-year">2018</span>
  </header>

  <section class="session-card session-left">
    <svg width="264" height="342" viewBox="0 0 264 342">
      <polygon points="0,88 60,70 200,70 264,88 264,342 0,342" fill="#a6ff00"/>
      <polyline points="0,88 60,70" stroke="#8b0a0a" stroke-width="6" fill="none"/>
      <polyline points="200,70 264,88" stroke="#8b0a0a" stroke-width="6" fill="none"/>
      <circle cx="130" cy="79" r="67" fill="#6c9a3c" stroke="#8b0a0a" stroke-width="5" role="img" aria-label="Photo of two golfers on the course"/>
    </svg>
    <p class="session-time">9:00 a.m- 11:00 a.m</p>
    <p class="session-desc">Shot gun Start for 18 hole players</p>
  </section>

  <section class="session-card session-right">
    <svg width="264" height="342" viewBox="0 0 264 342">
      <polygon points="0,88 60,70 200,70 264,88 264,342 0,342" fill="#a6ff00"/>
      <polyline points="0,88 60,70" stroke="#8b0a0a" stroke-width="6" fill="none"/>
      <polyline points="200,70 264,88" stroke="#8b0a0a" stroke-width="6" fill="none"/>
      <circle cx="133" cy="74" r="65" fill="#5e9a34" stroke="#8b0a0a" stroke-width="5" role="img" aria-label="Photo of a golfer teeing off on a fairway"/>
    </svg>
    <p class="session-time">11.30am - 12:00p.m</p>
    <p class="session-desc">Clinic with a Golf<br>Pro for non-Golfers</p>
  </section>

  <div class="date-ball">
    <div class="date-day">22</div>
    <div class="date-month">OCTOBER 2018</div>
  </div>

  <section class="lunch-panel">
    <h2 class="lunch-title">POST GOLF LUNCH</h2>
    <p class="lunch-info"><span class="label">From 1pm in the Dining Room</span><br><span class="label">Guest Speaker:</span> Alex Morton</p>
    <p class="lunch-pay"><span class="label">Payment:</span> www.example.com/payments<br><span class="label">Pricing:</span> 30$</p>
  </section>

  <footer class="footer-band">A combined Harlowe Old Scholars and Parents &amp; Friends Function.</footer>
</main>
</body>
</html>
```